Quorvix Letter head

Quorvix is a young and energetic software development consultancy. We spend our time working with clients to turn what ever is in their heads in to software.
We are trying to create an image of a high class software boutique who build class leading bespoke solutions.
We need a sharp letter head that looks great on high quality media.
We like bold colours and distinctive design. So show us what you can do.
Industry/Entity Type
Software
Requirements
Must have
- Our company is based in the UK and are requried to have on the paper somewhere the following information:
* Registered company name: Quorvix Ltd
* Registered company number
* VAT registration number
In addition we also want the following:
* An email address
* Telephone number
* Website address
An example of what some pages have in their footer is something like the following:
Quorvix Ltd is registered in England and Wales. Reg. no: 5316274
Registered office: 48 Cobblewick Road, Harlow Essex, CM93TP. Tel: 07712365081
You do not have to use this sentance but please make sure your design incorporates accommodates the requirements for UK based companies

```html
<!DOCTYPE html>
<html lang="en">
<head>
<meta charset="utf-8">
<title>Quorvix Letterhead</title>
<link rel="stylesheet" href="https://fonts.googleapis.com/css2?family=Montserrat:wght@300;400;600&display=swap">
<style>
  :root {
    --paper: #fbfaf7;
    --brand-red: #c8102e;
    --watermark: #f4e6e5;
    --text-grey: #555559;
  }
  html, body {
    margin: 0;
    padding: 0;
    overflow: hidden;
    background: var(--paper);
  }
  .letterhead {
    position: relative;
    width: 848px;
    height: 1200px;
    background: var(--paper);
    overflow: hidden;
    font-family: "Montserrat", Arial, sans-serif;
  }
  .frame-line {
    position: absolute;
    inset: 0;
  }
  .brand-name {
    position: absolute;
    left: 172px;
    top: 18px;
    margin: 0;
    font-size: 46px;
    font-weight: 400;
    letter-spacing: 1px;
    color: var(--brand-red);
    line-height: 1;
  }
  .brand-watermark {
    position: absolute;
    left: 0;
    width: 848px;
    top: 500px;
    text-align: center;
    font-size: 140px;
    font-weight: 300;
    color: var(--watermark);
    line-height: 1;
    user-select: none;
  }
  .company-details {
    position: absolute;
    left: 680px;
    top: 1124px;
    width: 146px;
    font-size: 5.6px;
    line-height: 1.42;
    color: var(--text-grey);
    white-space: nowrap;
  }
  .company-details .company-title {
    text-align: right;
    font-weight: 600;
    font-size: 6.4px;
  }
  .company-details .detail-row {
    display: flex;
  }
  .company-details .detail-label {
    width: 30px;
    flex-shrink: 0;
  }
</style>
</head>
<body>
  <main class="letterhead">
    <svg class="frame-line" width="848" height="1200" viewBox="0 0 848 1200" aria-hidden="true">
      <path d="M522 0 V56 A46 46 0 0 1 476 102 H104 A56 56 0 0 0 48 158 V1058 A56 56 0 0 0 104 1114 H848"
            fill="none" stroke="var(--brand-red)" stroke-width="4.5"/>
    </svg>

    <h1 class="brand-name">Quorvix</h1>

    <div class="brand-watermark" aria-hidden="true">Quorvix</div>

    <footer class="company-details">
      <div class="company-title">Quorvix Ltd</div>
      <div>48 Cobblewick Road, Harlow Essex, CM93TP</div>
      <div>Registered in England and Wales</div>
      <div class="detail-row"><span class="detail-label">Reg. no -</span><span>5316274</span></div>
      <div class="detail-row"><span class="detail-label">VAT no -</span><span>GB 482 7193 56</span></div>
      <div class="detail-row"><span class="detail-label">Website -</span><span>www.quorvixsoft.com</span></div>
      <div class="detail-row"><span class="detail-label">E-mail -</span><span>hello@quorvixsoft.com</span></div>
      <div class="detail-row"><span class="detail-label">Phone -</span><span>07712365081 , 0958-31729046</span></div>
    </footer>
  </main>
</body>
</html>
```